Pillow Company needs Pillow Insert Design

I just started a new pillow line with two pillow types. I have a hotel pillow and an organic pillow. I need two pillow insert signs designed that follow the same layout but are different color types. I want one sign to incorporate silver and white look and another sign to incorporate a green and white look (this one to look organic). They must have the same layout but different colors. I have include examples of what I want it to look like. In addition, I have uploaded the two hi res images for each sign. My logo is uploaded too.

I am open to other concepts and colors as long as it looks modern, clean and upscale. In addition, I need a Made in the USA logo on the pillow insert designs.

I have attached details on sign, images to be used, and examples that I like.

The Pillow Sign Size is 12 inches x 12 inches.

```html
<!DOCTYPE html>
<html lang="en">
<head>
<meta charset="utf-8">
<title>RestWell Pillow Insert Signs</title>
<link rel="stylesheet" href="https://fonts.googleapis.com/css2?family=Archivo:wght@300;400;700;800;900&display=swap">
<style>
  :root {
    --page-bg: #ffffff;
    --card-bg: #ffffff;
    --brand-green: #5aa83c;
    --tagline-green: #4f8f3a;
    --body-grey: #555a5c;
    --organic-title: #7b8a56;
    --organic-band: #7e8a6d;
    --organic-photo-a: #e9e4de;
    --organic-photo-b: #c7a58e;
    --hotel-title: #586f80;
    --hotel-band: #87a0bd;
    --hotel-photo-a: #e8ecef;
    --hotel-photo-b: #c9b7a6;
    --badge-red: #d7272e;
    --badge-blue: #2b3f8f;
    --white: #ffffff;
  }
  * { margin: 0; padding: 0; box-sizing: border-box; }
  html, body { width: 1200px; height: 1000px; overflow: hidden; background: var(--page-bg); }
  body { position: relative; font-family: "Archivo", Arial, sans-serif; }

  .sign {
    position: absolute;
    width: 542px; height: 541px;
    background: var(--card-bg);
    box-shadow: 2px 3px 5px rgba(0,0,0,0.35);
  }
  .sign--organic { left: 53px; top: 177px; --title: var(--organic-title); --band: var(--organic-band); --photo-a: var(--organic-photo-a); --photo-b: var(--organic-photo-b); }
  .sign--hotel { left: 605px; top: 283px; --title: var(--hotel-title); --band: var(--hotel-band); --photo-a: var(--hotel-photo-a); --photo-b: var(--hotel-photo-b); }

  .brand { position: absolute; left: 25px; top: 26px; display: flex; align-items: center; gap: 18px; }
  .brand__mark { width: 44px; height: 44px; background: var(--brand-green); }
  .brand__name { font-size: 23px; font-weight: 700; color: var(--brand-green); letter-spacing: 0.2px; }

  .tagline {
    position: absolute; left: 23px; top: 80px;
    font-size: 16.5px; font-weight: 300; line-height: 17px;
    color: var(--tagline-green); letter-spacing: 0.4px;
  }
  .intro {
    position: absolute; left: 23px; top: 124px; width: 270px;
    font-size: 9.6px; line-height: 11.2px; color: var(--body-grey);
  }

  .product-title {
    position: absolute; right: 27px; top: 38px;
    text-align: right; font-size: 30px; font-weight: 900; line-height: 36px;
    color: var(--title); letter-spacing: 0.3px;
  }
  .product-promise {
    position: absolute; right: 27px; top: 113px;
    text-align: right; font-size: 15.5px; line-height: 17.5px;
    color: var(--title);
  }

  .photo {
    position: absolute; left: 8px; top: 180px; width: 524px; height: 236px;
    background: linear-gradient(180deg, rgba(255,255,255,1) 0%, var(--photo-a) 30%, var(--photo-b) 70%, var(--photo-a) 100%);
  }

  .features {
    position: absolute; left: 8px; top: 416px; width: 524px; height: 118px;
    background: var(--band); color: var(--white);
  }
  .features__heading {
    position: absolute; left: 17px; top: 11px;
    font-size: 12.5px; font-weight: 800; letter-spacing: 0.3px;
  }
  .features__list {
    position: absolute; left: 17px; top: 28px; list-style: none;
    font-size: 9.4px; line-height: 11px;
  }
  .features__list li::before { content: "\2022\00a0"; }

  .origin {
    position: absolute; right: 17px; top: 12px; width: 150px; text-align: right;
  }
  .origin__badge { display: block; margin-left: auto; width: 68px; height: 40px; }
  .origin__label { margin-top: 8px; font-size: 10.5px; font-weight: 700; }
  .origin__note { margin-top: 3px; font-size: 8.4px; line-height: 10.5px; }
</style>
</head>
<body>

<section class="sign sign--organic">
  <div class="brand"><span class="brand__mark"></span><span class="brand__name">RestWell</span></div>
  <p class="tagline">SURROUND YOURSELF<br>WITH THE BEST!</p>
  <p class="intro">We added revolutionary features from our advanced Super Soft Premium Memory Foam that has an open cell structure design that recovers quickly and does not trap heat to our gel infused polyester fiber to our temperature managing Lyocera Fabric.</p>
  <h1 class="product-title">ALTERNATIVE<br>DOWN PILLOW</h1>
  <p class="product-promise">Especially designed to give<br>you the most comfortable<br>night's sleep in your life.</p>
  <div class="photo" role="img" aria-label="Photo of a couple relaxing together in a bed with white linens"></div>
  <div class="features">
    <h2 class="features__heading">DESIGNED FOR ALL TYPES OF SLEEP POSITIONS.</h2>
    <ul class="features__list">
      <li>Made From the Finest Premium Materials</li>
      <li>Adjusts to your Body Weight and Temperature</li>
      <li>100% Certified Organic Cotton Fabric</li>
      <li>Cool Non-Allergenic, Anti-Microbial, and Hypoallergenic</li>
      <li>Conforms to Head and Neck for optimal Alignment during sleep</li>
      <li>Mildew Proof and Dust Mite Resistant</li>
      <li>CertiFoam &reg; toxin free certified foam</li>
    </ul>
    <div class="origin">
      <svg class="origin__badge" viewBox="0 0 68 40" role="img" aria-label="Made in USA badge">
        <rect width="68" height="40" fill="var(--white)"/>
        <rect x="0" y="0" width="68" height="40" fill="var(--badge-red)" opacity="0.85"/>
        <rect x="0" y="0" width="28" height="20" fill="var(--badge-blue)"/>
      </svg>
      <p class="origin__label">Made In USA</p>
      <p class="origin__note">Surround Yourself with the Best!<br>Individually Handcrafted<br>and Made in USA</p>
    </div>
  </div>
</section>

<section class="sign sign--hotel">
  <div class="brand"><span class="brand__mark"></span><span class="brand__name">RestWell</span></div>
  <p class="tagline">SURROUND YOURSELF<br>WITH THE BEST!</p>
  <p class="intro">We added revolutionary features from our advanced Super Soft Premium Memory Foam that has an open cell structure design that recovers quickly and does not trap heat to our gel infused polyester fiber to our temperature managing Lyocera Fabric.</p>
  <h1 class="product-title">LUXURIOUS<br>PILLOW</h1>
  <p class="product-promise">Especially designed to give<br>you the most comfortable<br>night's sleep in your life.</p>
  <div class="photo" role="img" aria-label="Photo of a smiling family lying together on white pillows"></div>
  <div class="features">
    <h2 class="features__heading">DESIGNED FOR ALL TYPES OF SLEEP POSITIONS.</h2>
    <ul class="features__list">
      <li>Made From the Finest Premium Materials</li>
      <li>Adjusts to your Body Weight and Temperature</li>
      <li>Ventilated and Does Not Trap Heat</li>
      <li>Cool Non-Allergenic, Anti-Microbial, and Hypoallergenic</li>
      <li>Conforms to Head and Neck for optimal Alignment during sleep</li>
      <li>Mildew Proof and Dust Mite Resistant</li>
      <li>CertiFoam &reg; toxin free certified foam</li>
    </ul>
    <div class="origin">
      <svg class="origin__badge" viewBox="0 0 68 40" role="img" aria-label="Made in USA badge">
        <rect width="68" height="40" fill="var(--white)"/>
        <rect x="0" y="0" width="68" height="40" fill="var(--badge-red)" opacity="0.85"/>
        <rect x="0" y="0" width="28" height="20" fill="var(--badge-blue)"/>
      </svg>
      <p class="origin__label">Made In USA</p>
      <p class="origin__note">Surround Yourself with the Best!<br>Individually Handcrafted<br>and Made in USA</p>
    </div>
  </div>
</section>

</body>
</html>
```